Business Cards and Stationery for a laboratory quality consulting business
Brennick Quality Solutions
Creative Brief
Simple
Marion Brennick
Principal Consultant
4817 Thistlewood Lane Cary, NC 27604
marion@brennickquality.example
www.brennickquality.example

```html
<!DOCTYPE html>
<html lang="en">
<head>
<meta charset="utf-8">
<title>Brennick Quality Solutions — Business Card</title>
<link href="https://fonts.googleapis.com/css2?family=Poppins:wght@500;600;700&family=Nunito:wght@400;600&display=swap" rel="stylesheet">
<style>
  :root {
    --teal: #10877f;
    --orange: #f6a000;
    --ink: #4a4f55;
    --paper: #ffffff;
    --backdrop: #ffffff;
  }
  * { margin: 0; padding: 0; box-sizing: border-box; }
  html, body {
    width: 1200px;
    height: 901px;
    overflow: hidden;
    background: var(--backdrop);
  }
  .canvas {
    position: relative;
    width: 1200px;
    height: 901px;
  }
  .card {
    position: absolute;
    left: 233px;
    top: 238px;
    width: 717px;
    height: 410px;
    background: var(--paper);
    box-shadow: 0 2px 8px rgba(0, 0, 0, 0.12);
    overflow: hidden;
  }
  .corner-band {
    position: absolute;
    right: 0;
    top: 0;
    width: 407px;
    height: 41px;
  }
  .identity {
    position: absolute;
    left: 70px;
    top: 54px;
  }
  .identity__name {
    font-family: "Poppins", sans-serif;
    font-weight: 600;
    font-size: 33px;
    line-height: 1.1;
    color: var(--teal);
    letter-spacing: 0.5px;
  }
  .identity__role {
    margin-top: 2px;
    font-family: "Poppins", sans-serif;
    font-weight: 700;
    font-size: 15px;
    letter-spacing: 2.4px;
    color: var(--orange);
    padding-left: 22px;
  }
  .contact {
    position: absolute;
    left: 48px;
    top: 156px;
    font-family: "Nunito", sans-serif;
    font-size: 20px;
    color: var(--ink);
    list-style: none;
  }
  .contact__address {
    line-height: 26px;
    margin-bottom: 8px;
  }
  .contact__item {
    display: flex;
    align-items: center;
    gap: 10px;
    height: 40px;
  }
  .contact__icon {
    width: 26px;
    height: 26px;
    flex: none;
  }
  .brand {
    position: absolute;
    left: 410px;
    top: 206px;
    display: flex;
    align-items: center;
    gap: 14px;
  }
  .brand__dot {
    width: 72px;
    height: 72px;
    border-radius: 50%;
    background: var(--orange);
    flex: none;
  }
  .brand__name {
    font-family: "Poppins", sans-serif;
    font-weight: 600;
    font-size: 30px;
    line-height: 1.05;
    color: var(--teal);
  }
  .brand__name small {
    display: block;
    font-size: 17px;
    letter-spacing: 0.3px;
  }
  .footer-bar {
    position: absolute;
    bottom: 0;
    height: 33px;
  }
  .footer-bar--orange { left: 0; width: 562px; background: var(--orange); }
  .footer-bar--teal { left: 569px; width: 148px; background: var(--teal); }
</style>
</head>
<body>
<main class="canvas">
  <section class="card">
    <svg class="corner-band" viewBox="0 0 407 41" aria-hidden="true">
      <polygon points="0,0 407,0 407,41 40,41" fill="var(--teal)"/>
    </svg>

    <header class="identity">
      <h1 class="identity__name">Marion Brennick</h1>
      <p class="identity__role">Principal Consultant</p>
    </header>

    <ul class="contact">
      <li class="contact__address">4817 Thistlewood Lane Cary<br>NC 27604</li>
      <li class="contact__item">
        <svg class="contact__icon" viewBox="0 0 24 24" aria-hidden="true">
          <circle cx="12" cy="12" r="10.5" fill="none" stroke="var(--ink)" stroke-width="1.6"/>
          <path d="M8.6 6.8c.5-.4 1.1-.3 1.4.2l1 1.7c.3.5.2 1-.2 1.3l-.7.6c.6 1.4 1.6 2.5 3 3.2l.6-.7c.4-.4.9-.5 1.3-.2l1.7 1c.5.3.6.9.2 1.4l-.9 1c-.6.6-1.5.8-2.3.4-2.8-1.3-4.9-3.5-6.1-6.3-.3-.8-.1-1.7.5-2.3z" fill="var(--ink)"/>
        </svg>
        <span>919-555-0148</span>
      </li>
      <li class="contact__item">
        <svg class="contact__icon" viewBox="0 0 24 24" aria-hidden="true">
          <rect x="2" y="5" width="20" height="14" rx="1" fill="var(--ink)"/>
          <path d="M3 6l9 7 9-7" fill="none" stroke="#fff" stroke-width="1.6"/>
        </svg>
        <span>marion@brennickquality.example</span>
      </li>
      <li class="contact__item">
        <svg class="contact__icon" viewBox="0 0 24 24" aria-hidden="true">
          <circle cx="12" cy="12" r="10" fill="var(--ink)"/>
          <path d="M7 6c2 1 2 3 4 3s1 3-1 4-1 4-3 4M15 4c-1 2 1 3 2 4s3 1 3 3-2 2-3 4" fill="none" stroke="#fff" stroke-width="1.4"/>
        </svg>
        <span>www.brennickquality.example</span>
      </li>
    </ul>

    <div class="brand">
      <span class="brand__dot" aria-hidden="true"></span>
      <p class="brand__name">Brennick<small>Quality Solutions</small></p>
    </div>

    <div class="footer-bar footer-bar--orange"></div>
    <div class="footer-bar footer-bar--teal"></div>
  </section>
</main>
</body>
</html>
```